Brindle Capital and Investments

Create a simple business card design using the logos attached. Make it similar but not exact to the reference photo. Brand guidelines are also included.

```html
<!DOCTYPE html>
<html lang="en">
<head>
<meta charset="utf-8">
<title>Brindle Capital – Business Card</title>
<link rel="stylesheet" href="https://fonts.googleapis.com/css2?family=Questrial&display=swap">
<style>
  :root {
    --page-bg: #e9e6e1;
    --card-navy: #0a1142;
    --accent-copper: #b8621d;
    --text-white: #ffffff;
    --text-soft: #dfe2ee;
    --card-shadow: rgba(10, 17, 66, 0.28);
  }
  * { box-sizing: border-box; margin: 0; padding: 0; }
  html, body {
    width: 1200px;
    height: 900px;
    overflow: hidden;
    background: var(--page-bg);
    font-family: "Questrial", "Century Gothic", sans-serif;
  }
  .sheet {
    width: 1200px;
    height: 900px;
    display: flex;
    flex-direction: column;
    align-items: center;
    justify-content: center;
    gap: 48px;
  }
  .card {
    width: 640px;
    height: 366px;
    background: var(--card-navy);
    border-radius: 40px;
    box-shadow: 0 18px 36px var(--card-shadow);
    position: relative;
    color: var(--text-white);
    overflow: hidden;
  }

  /* Shared brand block */
  .brand {
    display: flex;
    align-items: center;
    gap: 14px;
  }
  .brand-dot {
    flex: none;
    width: 22px;
    height: 22px;
    border-radius: 50%;
    background: var(--accent-copper);
  }
  .brand-name {
    font-size: 34px;
    letter-spacing: 6px;
    text-transform: uppercase;
    color: var(--text-white);
    white-space: nowrap;
  }

  /* Front */
  .card-front {
    display: flex;
    flex-direction: column;
    align-items: center;
    justify-content: center;
  }
  .front-rule {
    width: 420px;
    height: 1px;
    margin: 30px 0 18px;
    background: linear-gradient(90deg, transparent, var(--accent-copper) 20%, var(--accent-copper) 80%, transparent);
  }
  .front-web {
    font-size: 17px;
    letter-spacing: 6px;
    color: var(--text-white);
  }
  .front-web .domain { color: var(--accent-copper); }

  /* Back */
  .card-back {
    display: flex;
    align-items: center;
  }
  .back-brand {
    flex: none;
    width: 300px;
    display: flex;
    justify-content: center;
  }
  .back-brand .brand {
    flex-direction: column;
    gap: 16px;
  }
  .back-brand .brand-dot { width: 20px; height: 20px; }
  .back-brand .brand-name {
    font-size: 28px;
    letter-spacing: 5px;
    line-height: 1.25;
    text-align: center;
  }
  .back-divider {
    flex: none;
    width: 1px;
    height: 190px;
    background: var(--accent-copper);
  }
  .contact {
    padding-left: 34px;
    font-size: 16px;
    line-height: 1.3;
    color: var(--text-soft);
  }
  .contact-name {
    font-size: 19px;
    color: var(--accent-copper);
    text-transform: uppercase;
    letter-spacing: 0.5px;
  }
  .contact-role { margin-bottom: 16px; }
  .contact-address { margin-bottom: 16px; }
  .contact-list { list-style: none; }
  .contact-list li {
    display: flex;
    align-items: center;
    gap: 10px;
    margin-bottom: 4px;
    white-space: nowrap;
  }
  .contact-list strong { color: var(--text-white); font-weight: 400; }
  .contact-icon { width: 15px; height: 15px; flex: none; }
</style>
</head>
<body>
<main class="sheet">

  <section class="card card-front" aria-label="Card front">
    <div class="brand">
      <span class="brand-dot"></span>
      <span class="brand-name">Brindle Capital</span>
    </div>
    <div class="front-rule"></div>
    <p class="front-web">www.<span class="domain">brindlecapital</span>.com</p>
  </section>

  <section class="card card-back" aria-label="Card back">
    <div class="back-brand">
      <div class="brand">
        <span class="brand-dot"></span>
        <span class="brand-name">Brindle<br>Capital</span>
      </div>
    </div>
    <div class="back-divider"></div>
    <div class="contact">
      <p class="contact-name">Jordan Hale</p>
      <p class="contact-role">Director</p>
      <p class="contact-address">00 dummy city<br>dummy place 0000</p>
      <ul class="contact-list">
        <li>
          <svg class="contact-icon" viewBox="0 0 16 16" aria-hidden="true">
            <path d="M3 1.5l3 3-1.6 1.8c.9 1.9 2.4 3.4 4.3 4.3L10.5 9l3 3-1.8 2.2C6.8 14 2 9.2 1.8 4.3z" fill="var(--accent-copper)"/>
          </svg>
          <span>300-200-4100</span>
        </li>
        <li>
          <svg class="contact-icon" viewBox="0 0 16 16" aria-hidden="true">
            <rect x="1" y="3" width="14" height="10" fill="var(--accent-copper)"/>
            <path d="M1 3l7 5.5L15 3" fill="none" stroke="var(--card-navy)" stroke-width="1.3"/>
          </svg>
          <span>info@<strong>brindlecapital</strong>.com</span>
        </li>
        <li>
          <svg class="contact-icon" viewBox="0 0 16 16" aria-hidden="true">
            <g fill="none" stroke="var(--accent-copper)" stroke-width="1.2">
              <circle cx="8" cy="8" r="6.5"/>
              <ellipse cx="8" cy="8" rx="3" ry="6.5"/>
              <path d="M1.5 8h13M2.5 5h11M2.5 11h11"/>
            </g>
          </svg>
          <span>www.<strong>brindlecapital</strong>.com</span>
        </li>
      </ul>
    </div>
  </section>

</main>
</body>
</html>
```